book cover self-publishing dystopia autism

I'm looking for an attractive cover to increase sales of my self-published book.
The book is a dystopia science fiction that addresses the subject of autism.
The title is Vorna. The name of the author is Ingrid PALLOW. which must appear on the first cover
Expected: 1st cover, 1st cover and 4th cover, for paper and ebook version

The story takes place on earth, not in space. A software manages the daily lives of people, it could be illustrated or not. Two communities are opposed. The book is written in the first person singular, which is the heroine of an 18-year-old woman. The story takes place in Europe, in a rural universe architecture metal glass, with a futuristic metro

The synopsis: Dorothee is part of the Elite. She will soon reach her 13th Rainbow, she hopes to be part of the Vorna Leaders. She wants to know if anyone can take her place for the next six months. She's going to do everything she can to find out, but she's also going to find out more and question her certainties about Vorna. His contacts with the Inferior gradually broke down the barriers separating them. However, it is social contacts that have defined the distinction between Elite and Inferior. In the past, the members of the Elite were a stigmatized minority, the autistic and the Inferior the norm, the neurotypical. And if Dorothee's perfect world was not just, should it be preserved or destroyed?

Target Market(s)

The book is aimed at a young adult or adolescent audience

Requirements
Must have
• An ISBN barcode will be placed in a 50.8 mm (2 in.) X 30.5 mm (1.2 in.) White frame in the lower right corner of the back cover.

Cover page size 1 and 4: 12.7 x 20.32cm
Template for the attached cover

Include the price of the book in 4th cover: 9.95 € TTC

Include on the 1st and 4th cover the author's name "Ingrid Pallow" and the title "Vorna"

Synopsis in 4th cover in French:

Dorothée is part of the Elite. She will soon reach her 13th Rainbow, so she hopes to be part of Vorna's Leaders. She wants at all costs to know if someone can take her place during the next 6 months. She will do everything to find out, but she will also discover much more and question her certainties about Vorna. His contacts with the Inferior gradually break down the barriers that separate them. Yet it is the social contacts that defined the distinction between Elite and Inferior. In the past, the Elite were a stigmatized minority, the autistic and the Inferior the norm, the neurotypical. And if Dorothee's perfect world wasn't fair, should it be preserved or destroyed?

```html
<!DOCTYPE html>
<html lang="en">
<head>
<meta charset="utf-8">
<title>Vorna – Ingrid PALLOW</title>
<link rel="stylesheet" href="https://fonts.googleapis.com/css2?family=Montserrat:wght@200;500&display=swap">
<style>
  :root {
    --cover-black: #000000;
    --ink-white: #ffffff;
    --puzzle-purple: #9900cc;
    --puzzle-navy: #003399;
    --puzzle-sky: #0a9be8;
    --puzzle-green: #339966;
    --puzzle-lime: #33cc33;
    --planet-ocean: #d6effc;
    --planet-land: #369a6a;
    --planet-sand: #cc9933;
    --planet-rim: #003399;
  }
  html, body {
    margin: 0;
    padding: 0;
    width: 850px;
    height: 1200px;
    overflow: hidden;
    background: var(--cover-black);
  }
  .book-cover {
    position: relative;
    width: 850px;
    height: 1200px;
    background: var(--cover-black);
    overflow: hidden;
    font-family: "Montserrat", sans-serif;
    color: var(--ink-white);
  }
  .book-title {
    position: absolute;
    top: 62px;
    left: 0;
    width: 100%;
    margin: 0;
    text-align: center;
    font-weight: 200;
    font-size: 232px;
    line-height: 1;
    letter-spacing: -2px;
  }
  .cover-art {
    position: absolute;
    inset: 0;
    width: 850px;
    height: 1200px;
  }
  .author-name {
    position: absolute;
    left: 533px;
    top: 1088px;
    margin: 0;
    font-weight: 500;
    font-size: 30px;
    letter-spacing: 0.5px;
    white-space: nowrap;
  }
</style>
</head>
<body>
  <main class="book-cover">
    <h1 class="book-title">Vorna</h1>

    <svg class="cover-art" viewBox="0 0 850 1200" xmlns="http://www.w3.org/2000/svg">
      <defs>
        <linearGradient id="puzzle-tones" x1="0" y1="0" x2="0.3" y2="1">
          <stop offset="0" stop-color="var(--puzzle-purple)"/>
          <stop offset="0.45" stop-color="var(--puzzle-navy)"/>
          <stop offset="0.8" stop-color="var(--puzzle-sky)"/>
          <stop offset="1" stop-color="var(--puzzle-sky)"/>
        </linearGradient>
        <linearGradient id="puzzle-corner" x1="0" y1="0" x2="0" y2="1">
          <stop offset="0" stop-color="var(--puzzle-green)"/>
          <stop offset="1" stop-color="var(--puzzle-lime)"/>
        </linearGradient>
        <radialGradient id="planet-glow" cx="0.5" cy="0.5" r="0.5">
          <stop offset="0.78" stop-color="#ffffff" stop-opacity="0.9"/>
          <stop offset="1" stop-color="#ffffff" stop-opacity="0"/>
        </radialGradient>
        <linearGradient id="planet-tones" x1="0.2" y1="0.1" x2="0.8" y2="0.95">
          <stop offset="0" stop-color="var(--planet-ocean)"/>
          <stop offset="0.35" stop-color="var(--planet-land)"/>
          <stop offset="0.6" stop-color="var(--planet-ocean)"/>
          <stop offset="0.85" stop-color="var(--planet-sand)"/>
        </linearGradient>
      </defs>

      <g class="puzzle-area" role="img" aria-label="Illustration of interlocking coloured puzzle pieces in purple, blue and green">
        <polygon points="0,414 300,700 538,955 300,1200 0,1200" fill="url(#puzzle-tones)"/>
        <polygon points="0,1000 180,1200 0,1200" fill="url(#puzzle-corner)"/>
      </g>

      <g class="planet-area" role="img" aria-label="Illustration of a small floating planet with clouds, green land and sandy continents">
        <circle cx="574" cy="650" r="250" fill="url(#planet-glow)"/>
        <circle cx="574" cy="650" r="210" fill="url(#planet-tones)" stroke="var(--planet-rim)" stroke-width="5"/>
      </g>
    </svg>

    <p class="author-name">Ingrid PALLOW</p>
  </main>
</body>
</html>
```